Folded A4 flyer for design&construction company

Folded A4 flyer needed. Keywords: elegant, stylish
our website www.corvimo.ae

Industry/Entity Type

Construction

```html
<!DOCTYPE html>
<html lang="en">
<head>
<meta charset="utf-8">
<title>Corvimo – Folded A4 Flyer</title>
<link rel="stylesheet" href="https://fonts.googleapis.com/css2?family=Arimo:wght@400;700&family=Tinos:wght@700&display=swap">
<style>
  :root{
    --bg:#5a5a5a;
    --paper:#ffffff;
    --orange:#f0821e;
    --orange-deep:#e8661a;
    --teal:#13907e;
    --teal-dark:#0f7a6c;
    --teal-light:#1a9c86;
    --ink:#2b2b2b;
    --muted:#555;
    --gold:#b98a32;
  }
  *{box-sizing:border-box;margin:0;padding:0}
  html,body{width:1200px;height:900px;overflow:hidden}
  body{background:var(--bg);font-family:"Arimo",Arial,sans-serif;position:relative}
  .page{position:absolute;top:190px;width:368px;height:520px;background:var(--paper);overflow:hidden;box-shadow:0 6px 18px rgba(0,0,0,.35)}
  .cover{left:28px}
  .spread{position:absolute;left:436px;top:190px;width:736px;height:520px;box-shadow:0 6px 18px rgba(0,0,0,.35)}
  .spread .page{top:0;box-shadow:none}
  .spread .inner-left{left:0;border-right:1px solid #e3e3e3}
  .spread .inner-right{left:368px}
  .cover-shapes{position:absolute;inset:0}
  .brand{position:absolute;display:flex;align-items:center;gap:5px;color:var(--ink);font-family:"Arimo",Arial,sans-serif;font-weight:400;letter-spacing:1.5px}
  .brand-dot{width:7px;height:7px;border-radius:50%;background:var(--gold)}
  .cover .brand{top:30px;right:22px;font-size:22px}
  .intro{position:absolute;left:18px;top:333px;width:335px;color:#fff;font-size:9.4px;line-height:1.27;text-align:justify}
  .cta{position:absolute;left:22px;top:433px;font-family:"Tinos","Times New Roman",serif;font-weight:700;color:var(--teal);font-size:17px;line-height:1.02}
  .contact{position:absolute;left:22px;top:490px;width:284px;font-size:7px;line-height:1.3;color:var(--ink)}
  .skyline{position:absolute;right:10px;bottom:10px;width:44px;height:30px;background:linear-gradient(#4a4a4a,#262626)}
  .section{position:absolute;left:0;width:368px;height:250px}
  .section.upper{top:14px}
  .section.lower{top:268px}
  .tag{position:absolute;left:18px;top:10px;height:22px;padding:0 30px 0 10px;background:var(--teal);color:#fff;font-size:12px;line-height:22px;letter-spacing:.5px;clip-path:polygon(0 0,100% 0,90% 100%,0 100%)}
  .tag-accent{position:absolute;top:24px;width:22px;height:8px;background:var(--orange);clip-path:polygon(30% 0,100% 0,70% 100%,0 100%)}
  .section .brand{left:24px;top:44px;font-size:17px}
  .services{position:absolute;left:26px;top:74px;list-style:none;font-size:9.5px;color:var(--ink);line-height:1.55;z-index:2}
  .services small{display:block;font-size:6.5px;line-height:1;color:var(--muted)}
  .photo{position:absolute;top:26px;right:12px;width:240px;height:214px}
  .photo-design{background:linear-gradient(90deg,rgba(255,255,255,1) 0%,rgba(255,255,255,0) 40%),linear-gradient(135deg,#e9d9b8,#8a5a22 45%,#3e2612 85%)}
  .photo-landscape{background:linear-gradient(90deg,rgba(255,255,255,1) 0%,rgba(255,255,255,0) 40%),linear-gradient(160deg,#6f8ea0,#1d3a55 40%,#c79a2e 70%,#2a3a3a)}
  .photo-fitout{background:linear-gradient(90deg,rgba(255,255,255,1) 0%,rgba(255,255,255,0) 40%),linear-gradient(170deg,#d8d8d8,#6a6a6a 50%,#1e1e1e)}
  .photo-maintenance{background:linear-gradient(90deg,rgba(255,255,255,1) 0%,rgba(255,255,255,0) 40%),linear-gradient(135deg,#e6e6e6,#a8a8a8 50%,#3a3a3a 80%,#b08a3a)}
</style>
</head>
<body>

<section class="page cover" aria-label="Front cover">
  <svg class="cover-shapes" viewBox="0 0 368 520" aria-hidden="true">
    <polygon points="0,0 250,0 0,235" fill="var(--orange)"/>
    <polygon points="30,320 150,170 368,120 368,320" fill="var(--teal-light)"/>
    <rect x="0" y="326" width="368" height="92" fill="var(--teal-dark)"/>
    <polygon points="300,428 314,418 368,418 368,428" fill="var(--orange)"/>
    <polygon points="340,520 368,502 368,520" fill="var(--orange-deep)"/>
  </svg>
  <div class="brand"><span class="brand-dot"></span>CORVIMO</div>
  <p class="intro">We believe in quality beginnings and flawless finishes. We are a team of creative designers and constructors with years of experience and expertise in providing complete interior design and construction services. Our unique designing prowess is complemented by our unflinching commitment to quality construction. Our team specializes in classic and contemporary high quality construction in Dubai for commercial and residential projects.</p>
  <h2 class="cta">GET A<br>FREE QUOTE<br>TODAY!</h2>
  <p class="contact">800 - CORVIMO / contact@corvimo.ae<br>www.corvimo.ae | Corvimo LLC, Marlow Tower, Office 1304, Business Bay, Dubai</p>
  <div class="skyline" role="img" aria-label="Small city skyline with construction cranes"></div>
</section>

<div class="spread" aria-label="Inside spread">
  <section class="page inner-left">
    <div class="section upper">
      <div class="photo photo-design" role="img" aria-label="Photo of an ornate classic interior with chandelier"></div>
      <div class="tag">DESIGN</div><div class="tag-accent" style="left:112px"></div>
      <div class="brand"><span class="brand-dot"></span>CORVIMO</div>
      <ul class="services">
        <li>Villas Interior Design</li><li>Villas Exterior Design</li><li>Landscape Design</li>
        <li>Retail Interior Design</li><li>Office Interior Design</li><li>Hospitality Interior Design</li>
        <li>Hotel Interior Design</li><li>Hotel Exterior Design</li><li>Restaurant Interior Design</li>
      </ul>
    </div>
    <div class="section lower">
      <div class="photo photo-landscape" role="img" aria-label="Photo of a waterfront city skyline at night"></div>
      <div class="tag">LANDSCAPING</div><div class="tag-accent" style="left:150px"></div>
      <div class="brand"><span class="brand-dot"></span>CORVIMO</div>
      <ul class="services">
        <li>Soft Landscaping</li><li>Irrigation Solutions</li><li>Hard land Scaping</li>
        <li>External Lighting</li><li>Swimming Pool &amp; Water Features</li>
      </ul>
    </div>
  </section>

  <section class="page inner-right">
    <div class="section upper">
      <div class="photo photo-fitout" role="img" aria-label="Black and white photo of people at a glass office window overlooking a city"></div>
      <div class="tag">FITOUT</div><div class="tag-accent" style="left:104px"></div>
      <div class="brand"><span class="brand-dot"></span>CORVIMO</div>
      <ul class="services">
        <li>Development Approvals</li><li>Flooring Solutions</li><li>Partition</li>
        <li>Sealing Solutions</li><li>MEP Works</li><li>Civil Works</li><li>Joinery</li>
        <li>Glass and Aluminium Works<small>(subcontractor)</small></li>
      </ul>
    </div>
    <div class="section lower">
      <div class="photo photo-maintenance" role="img" aria-label="Photo of a concrete building facade under construction"></div>
      <div class="tag">MAINTENANCE</div><div class="tag-accent" style="left:150px"></div>
      <div class="brand"><span class="brand-dot"></span>CORVIMO</div>
      <ul class="services">
        <li>AC Repair</li><li>Plumber Services</li><li>Electric Repair</li><li>Carpentry Work</li>
        <li>Gypsum Ceiling</li><li>Painting Services</li><li>Cleaning Services</li><li>Emergency Services</li>
      </ul>
    </div>
  </section>
</div>

</body>
</html>
```